40k Ultra High Pressure Waterblasing Ad

We need 1 page flyer ad for our industry's brochure/membership directory.
We're a manufacturer & supplier for the Ultra High Pressure Waterblasting industry.
We'd like the ad to be simple and clean, highlighting some of our parts. Our dedication to our customers and affordable prices.
Some of the parts are Dorvel Mastrick Hoses, Sapphire Nozzles, Rotating Jetlance.

Our website is torvaflux.com

Requirements
Must have
• Dorvel Mastrick 40k Hose
• Sapphire Nozzles
• Rotating Jetlance
• **Update - Would like to incorporate the "iron skein logo w/ bulldog" from uploaded dorvel iron skein hose attachment. Highlighting the hose's features.
Nice to have
• Brief Bullet points or something else highlighting what we sell.
• - Pump replacement parts
• - Sapphire Nozzles
• - Rotating Jetlance
• - Fittings and adapters
• - Safety Gear
• I've uploaded past ads we've used.
Should not have
• Lots of text area

```html
<!DOCTYPE html>
<html lang="en">
<head>
<meta charset="utf-8">
<title>Torvaflux Technologies – Waterjetting Products Flyer</title>
<link href="https://fonts.googleapis.com/css2?family=Roboto:ital,wght@0,300;0,400;0,500;0,700;1,700;1,900&display=swap" rel="stylesheet">
<style>
  :root{
    --navy:#23286b;
    --blue:#3f93d0;
    --blue-strip:#3d8fd0;
    --heading-blue:#3f8fcc;
    --ink:#1e2460;
    --bg:#2a2a2a;
    --white:#ffffff;
    --rule:#c9ccd3;
  }
  *{box-sizing:border-box;margin:0;padding:0}
  html,body{width:1200px;height:1200px;overflow:hidden;background:var(--bg);font-family:"Roboto",Arial,sans-serif}
  .flyer{position:absolute;left:192px;top:20px;width:816px;height:1160px;background:var(--white);overflow:hidden}
  .diagonal-band{position:absolute;left:0;top:0}
  .abs{position:absolute}

  .brand{left:58px;top:58px;display:flex;align-items:center;gap:10px}
  .brand-mark{width:22px;height:22px;border-radius:50%;background:var(--blue)}
  .brand-name{font-size:64px;font-weight:700;color:var(--navy);letter-spacing:1px;line-height:1}

  .call{left:267px;top:58px;color:var(--navy);font-weight:900;font-style:italic;line-height:1.05;z-index:2}
  .call-label{font-size:34px}
  .call-number{font-size:35px;letter-spacing:.5px}

  .photo{border-radius:6px}
  .photo-nozzles{left:90px;top:287px;width:287px;height:101px;background:linear-gradient(180deg,#b7bcc2,#6f7780)}
  .photo-gun{left:366px;top:142px;width:321px;height:207px;background:linear-gradient(135deg,#c9cdd2,#7d8590 60%,#3b3f46)}
  .photo-hose{left:467px;top:377px;width:281px;height:203px;border-radius:50%;background:radial-gradient(ellipse at center,#ffffff 28%,#a6aeb8 30%,#7c8591 60%,#b9c0c8 72%,rgba(255,255,255,0) 74%)}

  .promo-strip{left:60px;top:427px;width:348px;height:18px;background:var(--blue-strip)}
  .promo-box{left:60px;top:454px;width:348px;height:200px;background:var(--blue);color:var(--white);padding:22px 30px 0}
  .promo-title{font-size:31px;font-weight:700;line-height:1.12;padding-bottom:10px;border-bottom:2px solid var(--white);width:282px}
  .promo-sub{font-size:31px;font-weight:700;margin-top:8px}

  .badge{top:591px;height:62px}
  .badge-one{left:441px;width:68px;border-radius:50%;background:#c8c4bd}
  .badge-two{left:524px;top:610px;width:105px;height:38px;background:#111}
  .badge-three{left:653px;width:107px;height:56px;background:#222;border-radius:30px 30px 4px 4px}

  .headline{left:0;top:698px;width:816px;text-align:center;font-size:49px;font-weight:300;color:var(--heading-blue);letter-spacing:.5px}

  .section-bar{height:32px;background:var(--navy);color:var(--white);font-size:17px;padding-left:13px;line-height:32px}
  .bar-pump{left:60px;top:792px;width:337px}
  .bar-hose{left:423px;top:792px;width:334px}
  .bar-features{left:60px;top:912px;width:697px}

  .bullets{list-style:none;font-size:12.5px;color:var(--ink);line-height:19px}
  .bullets li::before{content:"";display:inline-block;width:5px;height:5px;border-radius:50%;background:var(--ink);margin-right:5px;vertical-align:middle}
  .list-a{left:66px;top:837px}
  .list-b{left:223px;top:837px}
  .list-c{left:428px;top:836px}
  .list-d{left:586px;top:836px}

  .features{left:60px;top:960px;width:697px;height:83px;display:flex}
  .feature{flex:1;font-size:12.3px;color:var(--ink);line-height:16px;padding:0 8px 0 10px;border-right:1px solid var(--ink)}
  .feature:last-child{border-right:none;flex:1.05}
  .feature .bullets{font-size:12.3px;line-height:16px}
  .feature .bullets li::before{margin-right:4px}

  .footer-rule{left:0;top:1073px;width:816px;height:2px;background:var(--rule)}
  .footer{left:0;top:1091px;width:816px;text-align:center;font-size:14.5px;color:var(--navy)}
  .footer .sep{margin:0 13px}
  .footer-band{left:0;top:1128px;width:816px;height:32px;background:var(--navy)}
</style>
</head>
<body>
<main class="flyer">
  <svg class="diagonal-band" width="816" height="1160" viewBox="0 0 816 1160" aria-hidden="true">
    <polygon points="0,306 816,2 816,352 0,655" fill="var(--navy)"/>
  </svg>

  <div class="abs brand">
    <span class="brand-name">TFT</span>
    <span class="brand-mark"></span>
  </div>

  <div class="abs photo photo-gun" role="img" aria-label="Photo of a high-pressure waterjetting gun"></div>
  <div class="abs photo photo-nozzles" role="img" aria-label="Photo of a row of stainless sapphire nozzle fittings"></div>
  <div class="abs photo-hose" role="img" aria-label="Photo of a coiled 40k high-pressure hose"></div>

  <div class="abs call">
    <div class="call-label">Call Now!</div>
    <div class="call-number">555-014-2290</div>
  </div>

  <div class="abs promo-strip"></div>
  <div class="abs promo-box">
    <h1 class="promo-title">QUALITY<br>WATERJETTING<br>PRODUCTS</h1>
    <p class="promo-sub">At Affordable Prices</p>
  </div>

  <div class="abs badge badge-one" role="img" aria-label="Partner badge"></div>
  <div class="abs badge badge-two" role="img" aria-label="Partner badge"></div>
  <div class="abs badge badge-three" role="img" aria-label="Partner badge"></div>

  <h2 class="abs headline">OUR CUSTOMERS COME FIRST</h2>

  <div class="abs section-bar bar-pump">Pump Replacement Parts</div>
  <div class="abs section-bar bar-hose">Dorvel Mastrick 40k Hose</div>

  <ul class="abs bullets list-a"><li>Sapphire Nozzles</li><li>Rotating Jetlance</li></ul>
  <ul class="abs bullets list-b"><li>Fittings and adapters</li><li>Safety Gear</li></ul>
  <ul class="abs bullets list-c"><li>Sapphire Nozzles</li></ul>
  <ul class="abs bullets list-d"><li>Rotating Jetlance</li></ul>

  <div class="abs section-bar bar-features">IRONSKEIN Hose Features</div>

  <div class="abs features">
    <p class="feature">IRONSKEIN abrasion resistant cover eliminates the obstructive PVC Cover</p>
    <p class="feature">Features HueSignal TM technology to provide early warning of hose wear</p>
    <p class="feature">Compact O.D&gt; reduces friction drag</p>
    <div class="feature">Lighter weight assemblies (up to 16%)
      <ul class="bullets"><li>reduces Friction and drag</li><li>reduces operator fatigue</li><li>reduces freight costs</li></ul>
    </div>
  </div>

  <div class="abs footer-rule"></div>
  <p class="abs footer">Torvaflux Technologies<span class="sep">|</span>Email: info@torvaflux.com<span class="sep">|</span>Ph: 555-014-2290<span class="sep">|</span>www.torvaflux.com</p>
  <div class="abs footer-band"></div>
</main>
</body>
</html>
```